Bed Company needs business card

Hello, we are a bed company that makes specialized magnets for beds. We are an alternative healing company. I need a modern and upscale business card. Please incorporate my logo for the card.

Accepted file formats are AI, EPS, and Press-Ready PDFS.

Please include all fonts or convert them to outlines regardless of file type.

If you are designing the card in Photoshop the file Must be 1200dpi.

I am open to anything for the business card.  I really like all of your designs and if you want to change the color of the logo, you can.  I will be making the final selection by Friday.  Thank You for all of your designs.  Feel Free to submit different color logos if you want.  

Reason: I will make a decision Final on Friday April 20th. 2012. Good Luck and Thank you all for the designs.

Target Market(s)

My target Market is people, who are looking for alternative healing.

Industry/Entity Type

Business

Requirements
Must have
• My logo must be incorporated. The front card must have

Name
Job Title

Address
Work
Cell
Fax
email
web

Just put in fake info for the card.

The back of the card. I want the logo on the back with color. I just want it to look modern and cool.

```html
<!DOCTYPE html>
<html lang="en">
<head>
<meta charset="utf-8">
<title>Restwell Business Card</title>
<link rel="stylesheet" href="https://fonts.googleapis.com/css2?family=Arimo:wght@400;700&family=Cousine&family=PT+Sans+Narrow:wght@400&display=swap">
<style>
  :root {
    --stage: #474644;
    --copper: #84482a;
    --espresso: #2e1a0e;
    --rule: #0d0907;
    --walnut: #4a2208;
    --paper: #ffffff;
    --ink: #111111;
  }
  html, body {
    margin: 0;
    padding: 0;
    width: 1200px;
    height: 1037px;
    overflow: hidden;
    background: var(--stage);
  }
  .canvas {
    position: relative;
    width: 1200px;
    height: 1037px;
  }

  /* Back of card */
  .card-back {
    position: absolute;
    left: 171px;
    top: 154px;
    width: 586px;
    height: 334px;
    background: var(--copper);
    overflow: hidden;
  }
  .brand {
    position: absolute;
    left: 90px;
    top: 108px;
    display: flex;
    align-items: center;
    gap: 18px;
    color: var(--espresso);
  }
  .brand-mark {
    width: 46px;
    height: 46px;
    background: var(--espresso);
  }
  .brand-text {
    display: flex;
    flex-direction: column;
  }
  .brand-name {
    font-family: "Arimo", Arial, sans-serif;
    font-weight: 700;
    font-size: 64px;
    line-height: 1;
    letter-spacing: -1px;
  }
  .brand-tagline {
    font-family: "PT Sans Narrow", Arial, sans-serif;
    font-size: 24px;
    line-height: 1.1;
    margin-top: 4px;
    margin-left: 4px;
  }
  .rule-thin {
    position: absolute;
    left: 0;
    top: 312px;
    width: 100%;
    height: 3px;
    background: var(--rule);
  }
  .rule-band {
    position: absolute;
    left: 0;
    bottom: 0;
    width: 100%;
    height: 10px;
    background: var(--rule);
  }

  /* Front of card */
  .card-front {
    position: absolute;
    left: 506px;
    top: 516px;
    width: 586px;
    height: 335px;
    background: var(--paper);
    overflow: hidden;
    color: var(--ink);
  }
  .card-edges {
    position: absolute;
    inset: 0;
  }
  .person-name {
    position: absolute;
    left: 269px;
    top: 40px;
    margin: 0;
    font-family: "Arimo", Arial, sans-serif;
    font-weight: 700;
    font-size: 21px;
    letter-spacing: 0.5px;
  }
  .person-title {
    position: absolute;
    left: 320px;
    top: 64px;
    margin: 0;
    font-family: "Cousine", "Courier New", monospace;
    font-size: 12px;
    letter-spacing: 1px;
  }
  .details {
    position: absolute;
    margin: 0;
    padding: 0;
    list-style: none;
    font-family: "PT Sans Narrow", Arial, sans-serif;
    text-transform: uppercase;
  }
  .details-main {
    left: 316px;
    top: 150px;
    font-size: 14px;
  }
  .details-main li { height: 26px; }
  .details-main li.small {
    font-size: 12.5px;
    height: 20px;
  }
  .details-main li.small:first-of-type { margin-top: 2px; }
  .details-phone {
    left: 65px;
    top: 206px;
    font-size: 12.5px;
  }
  .details-phone li { height: 19px; }
</style>
</head>
<body>
<main class="canvas">

  <section class="card-back" aria-label="Back of business card">
    <div class="brand">
      <div class="brand-mark"></div>
      <div class="brand-text">
        <span class="brand-name">Restwell</span>
        <span class="brand-tagline">Alternative Healing</span>
      </div>
    </div>
    <div class="rule-thin"></div>
    <div class="rule-band"></div>
  </section>

  <section class="card-front" aria-label="Front of business card">
    <svg class="card-edges" width="586" height="335" viewBox="0 0 586 335" aria-hidden="true">
      <path fill="#f4f4f4" d="M12 0 C30 80 45 150 38 220 C32 260 15 270 18 300 L22 335 L80 335 C70 300 60 270 70 230 C75 160 60 80 55 0 Z" opacity="0.6"/>
      <path fill="var(--walnut)" d="M0 0 L12 0 C30 80 45 150 38 220 C32 260 15 270 18 300 C20 320 22 335 22 335 L0 335 Z"/>
      <path fill="var(--walnut)" d="M586 0 L574 0 C560 80 548 160 555 240 C560 270 570 278 566 300 C562 320 565 335 565 335 L586 335 Z"/>
    </svg>

    <h1 class="person-name">DANIEL REYES</h1>
    <p class="person-title">MANAGING DIRECTOR</p>

    <ul class="details details-main">
      <li>Address: Harbor Square</li>
      <li>Work: Alternative Healing Company</li>
      <li class="small">Email: daniel@restwellhealing.com</li>
      <li class="small">Web: www.restwellhealing.com</li>
    </ul>

    <ul class="details details-phone">
      <li>Cell:05550123467</li>
      <li>Fax: 77305550198</li>
    </ul>
  </section>

</main>
</body>
</html>
```